Need a Halden & Co
* logo
* word and powerpoint livery
* basic webpage

Halden & Co is a Private M&A Advisor. We want to look like http://www.brightwickadvisory.example
It needs to communicate reliabity, conservativeness and discretion.

```html
<!DOCTYPE html>
<html lang="en">
<head>
<meta charset="utf-8">
<title>Halden &amp; Co — Private M&amp;A Advisor</title>
<link href="https://fonts.googleapis.com/css2?family=Hind:wght@400;500&family=Ubuntu:wght@500&display=swap" rel="stylesheet">
<style>
  :root {
    --brand: #1f63c4;
    --ink: #333333;
    --ink-soft: #555555;
    --muted: #777777;
    --band: #ececec;
    --rule: #cfcfcf;
    --link: #1b5f9e;
    --night-1: #0f2a52;
    --night-2: #16386b;
    --night-3: #3a2a1c;
  }
  * { box-sizing: border-box; margin: 0; padding: 0; }
  html, body { width: 1200px; height: 1069px; overflow: hidden; background: #fff; }
  body { font-family: "Hind", sans-serif; color: var(--ink); position: relative; }
  .page { position: absolute; left: 110px; top: 0; width: 980px; height: 1069px; }

  .site-header { position: relative; height: 105px; }
  .brand { position: absolute; left: 0; top: 20px; display: flex; align-items: center; gap: 10px; }
  .brand-mark { width: 22px; height: 22px; background: var(--brand); }
  .brand-name { font-family: "Ubuntu", sans-serif; font-weight: 500; font-size: 29px; color: var(--brand); letter-spacing: 0.5px; }
  .brand-tagline { position: absolute; left: 15px; top: 74px; font-size: 13px; letter-spacing: 1.6px; color: var(--ink-soft); }
  .search { position: absolute; right: 0; top: 65px; width: 157px; height: 24px; border: 1px solid #bdbdbd; display: flex; align-items: center; padding: 0 8px 0 11px; font-size: 10px; color: #888; justify-content: space-between; }

  .main-nav { height: 32px; background: var(--band); display: flex; }
  .main-nav a { display: flex; align-items: center; padding: 2px 11px 0; font-size: 13px; color: #222; text-decoration: none; border-right: 1px solid #fff; }
  .main-nav a:first-child { padding-left: 14px; }
  .main-nav a:last-child { border-right: 0; }

  .hero { position: relative; height: 329px; background: linear-gradient(180deg, var(--night-1) 0%, var(--night-2) 45%, var(--night-3) 62%, var(--night-1) 100%); }
  .hero-arrow { position: absolute; top: 155px; width: 43px; height: 41px; background: rgba(255,255,255,0.3); display: flex; align-items: center; justify-content: center; }
  .hero-arrow.prev { left: 25px; }
  .hero-arrow.next { right: 22px; }

  .welcome { text-align: center; padding-top: 26px; height: 190px; position: relative; }
  .welcome h1 { font-weight: 400; font-size: 21px; color: #222; margin-bottom: 9px; }
  .welcome p { font-size: 12.6px; line-height: 23px; color: var(--ink); }
  .divider { position: absolute; left: 60px; right: 60px; bottom: 0; height: 20px; background: radial-gradient(ellipse at 50% 0%, rgba(0,0,0,0.09), rgba(0,0,0,0) 70%); }

  .columns { display: flex; justify-content: space-between; padding-top: 35px; height: 341px; }
  .about { width: 470px; }
  .news { width: 466px; }
  .section-head { display: flex; align-items: center; gap: 14px; height: 40px; margin-bottom: 14px; }
  .section-head h2 { font-weight: 400; font-size: 21px; color: #222; padding-top: 4px; }
  .about p { font-size: 12.6px; line-height: 27px; color: var(--ink); }
  .more { display: inline-block; font-size: 12px; color: var(--link); text-decoration: none; margin-top: 1px; }

  .news-item { border-bottom: 1px solid var(--rule); padding: 0 0 8px; margin-bottom: 8px; margin-left: -5px; padding-left: 5px; }
  .news-item:last-of-type { border-bottom: 0; margin-bottom: 0; padding-bottom: 2px; }
  .news-date { font-size: 12px; color: var(--ink-soft); height: 27px; line-height: 27px; }
  .news-line { display: flex; justify-content: space-between; align-items: center; font-size: 12.6px; height: 22px; }

  .site-footer { position: absolute; left: 0; top: 988px; width: 980px; height: 81px; background: var(--band); text-align: center; padding-top: 20px; font-size: 12.6px; color: #222; }
  .footer-links a { color: #222; text-decoration: none; }
  .footer-links span { margin: 0 6px; }
  .copyright { margin-top: 8px; }
</style>
</head>
<body>
<div class="page">
  <header class="site-header">
    <div class="brand"><span class="brand-mark"></span><span class="brand-name">HALDEN &amp; CO</span></div>
    <div class="brand-tagline">Private M&amp;A Advisor</div>
    <div class="search"><span>Search</span>
      <svg width="12" height="12" viewBox="0 0 12 12"><circle cx="5" cy="5" r="3.8" fill="none" stroke="#888" stroke-width="1.4"/><line x1="7.8" y1="7.8" x2="11" y2="11" stroke="#888" stroke-width="1.6"/></svg>
    </div>
  </header>

  <nav class="main-nav">
    <a href="#">HOME</a><a href="#">ABOUT</a><a href="#">TEAM</a><a href="#">EXPERIENCE</a><a href="#">PRESS RELEASES</a><a href="#">CAREERS</a><a href="#">CONTACT</a>
  </nav>

  <section class="hero" role="img" aria-label="Night view of a city riverfront with lit towers reflected in the water">
    <span class="hero-arrow prev"><svg width="10" height="14" viewBox="0 0 10 14"><polyline points="8,1 2,7 8,13" fill="none" stroke="#fff" stroke-width="1.4"/></svg></span>
    <span class="hero-arrow next"><svg width="10" height="14" viewBox="0 0 10 14"><polyline points="2,1 8,7 2,13" fill="none" stroke="#fff" stroke-width="1.4"/></svg></span>
  </section>

  <section class="welcome">
    <h1>Welcome to the Halden &amp; Co</h1>
    <p>Lorem Ipsum is simply dummy text of the printing and typesetting industry. Lorem Ipsum has been the industry's standard dummy text ever since the 1500s, when an unknown printer took a galley of type and scrambled it to make a type specimen book. It has survived not only five centuries, but also the leap into electronic typesetting, remaining essentially unchanged. It was popularised in the 1960s with the release of Letraset sheets containing Lorem Ipsum passages, and more recently with desktop publishing software like Aldus PageMaker including versions of Lorem Ipsum.</p>
    <div class="divider"></div>
  </section>

  <div class="columns">
    <section class="about">
      <div class="section-head">
        <svg width="40" height="38" viewBox="0 0 40 38"><ellipse cx="20" cy="22" rx="16" ry="12" fill="#aaa"/><circle cx="24" cy="8" r="5" fill="#aaa"/><rect x="9" y="30" width="5" height="7" fill="#aaa"/><rect x="25" y="30" width="5" height="7" fill="#aaa"/><rect x="34" y="18" width="5" height="6" fill="#aaa"/></svg>
        <h2>About Us</h2>
      </div>
      <p>Lorem Ipsum is simply dummy text of the printing and typesetting industry. Lorem Ipsum has been the industry's standard dummy text ever since the 1500s, when an unknown printer took a galley of type and scrambled it to make a type specimen book. It has survived not only five centuries, but also the leap into electronic typesetting, remaining essentially unchanged. It was popularised in the 1960s with the release of Letraset sheets containing Lorem Ipsum passages, and more recently with desktop publishing software like Aldus PageMaker including versions of Lorem Ipsum.</p>
      <a class="more" href="#">CLICK HERE</a>
    </section>

    <section class="news">
      <div class="section-head">
        <svg width="42" height="34" viewBox="0 0 42 34"><rect x="1" y="1" width="40" height="32" fill="none" stroke="#aaa" stroke-width="2"/><rect x="7" y="8" width="13" height="12" fill="#aaa"/><rect x="23" y="8" width="12" height="2.5" fill="#aaa"/><rect x="23" y="13" width="12" height="2.5" fill="#aaa"/><rect x="23" y="18" width="12" height="2.5" fill="#aaa"/><rect x="7" y="24" width="28" height="2.5" fill="#aaa"/></svg>
        <h2>Latest News</h2>
      </div>
      <div class="news-item">
        <div class="news-date">Jul 10 2014</div>
        <div class="news-line"><span>Lorem Ipsum is simply dummy text of the printing and typesetting industry.</span>
          <svg width="9" height="16" viewBox="0 0 9 16"><polyline points="1,1 8,8 1,15" fill="none" stroke="#999" stroke-width="1.2"/></svg></div>
      </div>
      <div class="news-item">
        <div class="news-date">Jul 03 2014</div>
        <div class="news-line"><span>Lorem Ipsum is simply dummy text of the printing and typesetting industry.</span>
          <svg width="9" height="16" viewBox="0 0 9 16"><polyline points="1,1 8,8 1,15" fill="none" stroke="#999" stroke-width="1.2"/></svg></div>
      </div>
      <div class="news-item">
        <div class="news-date">Jun 10 2014</div>
        <div class="news-line"><span>Lorem Ipsum is simply dummy text of the printing and typesetting industry.</span>
          <svg width="9" height="16" viewBox="0 0 9 16"><polyline points="1,1 8,8 1,15" fill="none" stroke="#999" stroke-width="1.2"/></svg></div>
      </div>
      <a class="more" href="#">CLICK HERE</a>
    </section>
  </div>

  <footer class="site-footer">
    <div class="footer-links"><a href="#">Home</a><span>|</span><a href="#">Site Map</a><span>|</span><a href="#">Legal</a><span>|</span><a href="#">Contact</a><span>|</span><a href="#">Connect</a></div>
    <div class="copyright">Copyright © 2014 halden&amp;coAll Rights Reserved.</div>
  </footer>
</div>
</body>
</html>
```